Website Design for a different kind of Business Consulting organisation needed!

We need a website design that reflects who we are, the simplicity of our consulting business and with a focus on our priority - to help our clients deliver, or execute - the "e" in Vantor-o.

Our key high level requirements are:
1) Simple and intuitive look and feel
2) Integration with all key social media platforms, chirpline, friendwall, workmesh, blogvine.

10 pages, tops.
- Main page - Welcome
- About Us/ Who are Vantor-o?
- 5 services pages - Project Management, Business Process Management, Change Management, Business Analysis and Finance Systems
- Contact Us

Something like:
http://www.hlmworks.example/

Vantor-o is a registered trademark and all Logos and other branded material are attached for reference.

So, what’s our gig: A few snippets from previous work...

We are a different kind of business consulting group. We partner with our clients to help them deliver change. We don't just provide them with the theory. We also provide them with the leadership and capability to execute the change.

We aren’t a one stop shop, and we don’t offer cookie cutter solutions. We’re a boutique consulting firm covering Project Management, Business Process Management, Change Management and Business Analytics.

Vantor-o is a professional services organisation that partners with their clients to lead the execution of strategic process and system improvement initiatives. Vantor-o combines hands on delivery with coaching in best practice methodologies and approaches to build their clients capabilities to ensure their ongoing success in project implementations.

UPDATES:

Thanks to everyone who has submitted designs so far. The standard of designs coming through is quite high, with lots of professional designs that nail the design brief. Eliminating them is proving to be quite challenging.

A few updates to the job brief:
- Please make sure the design fits on one page. We would like all of our information to be on the first page that people see without them having to scroll down
- Please ensure you include the FIVE services we offer in the design
- Please use corporate images/snapvault photos in your designs which are relevant to our business
- Please add a section for a live chirpline feed from our chirpline account and a link to circlenet+
- Please add a section for news/updates

Also, if you are able to build a site once a design is selected, please let us know.

Thanks,

Marisol.

Target Market(s)

Our target customers are large enterprises in Australia that are growing rapidly and have recently (last 24 months) undertaken or are currently undergoing software implementations and business process improvement programs. These businesses have a turnover of $100m or above and are working hard to differentiate themselves from their competitors but are not seeing the return on investment promised by software vendors and process improvement initiatives.

Industry/Entity Type

Leadership

Requirements
Must have
• Collaboration / Training / Workshop / Consulting images all of a professional nature.
Simple, non-cluttered look with plenty of white space.

```html
<!DOCTYPE html>
<html lang="en">
<head>
<meta charset="utf-8">
<title>Vantor-o — Professional Services</title>
<link href="https://fonts.googleapis.com/css2?family=Open+Sans:wght@400;600;700&display=swap" rel="stylesheet">
<style>
:root{
  --brand:#0d4f9c;
  --brand-dark:#0b2f5e;
  --ink:#333;
  --muted:#6b6b6b;
  --line:#d6d6d6;
  --band:#efefef;
  --warm:#fbf8f7;
  --footer:#a9a9a9;
  --white:#fff;
}
*{margin:0;padding:0;box-sizing:border-box}
html,body{width:1055px;height:1200px;overflow:hidden;background:var(--white);font-family:"Open Sans",sans-serif;color:var(--ink)}
.page{position:relative;width:1055px;height:1200px;overflow:hidden}
.abs{position:absolute}
.top-rule{left:0;top:0;width:1055px;height:4px;background:var(--brand)}
.members-login{left:846px;top:0;width:75px;height:18px;background:var(--brand);color:var(--white);font-size:8px;font-weight:600;text-align:center;line-height:18px}
.header{left:0;top:4px;width:1055px;height:80px;border-bottom:1px solid var(--line)}
.logo{color:var(--brand);font-size:32px;font-weight:400;letter-spacing:.5px;line-height:1}
.site-logo{left:134px;top:25px}
.nav{left:430px;top:34px;display:flex;font-size:12px;color:#555}
.nav a{color:inherit;text-decoration:none;margin-right:38px;display:flex;align-items:center;gap:6px}
.nav a.active{color:var(--brand);font-weight:600}
.nav a:last-child{margin-right:0}
.hero{left:0;top:84px;width:1055px;height:335px;background:linear-gradient(90deg,#fafafa 0%,#f2f3f5 40%,#e9ebee 100%);border-bottom:1px solid var(--line)}
.hero-photo{left:430px;top:84px;width:505px;height:335px;background:radial-gradient(ellipse 60% 90% at 72% 65%,#2c3d62 0%,#4f6286 40%,rgba(190,200,214,.6) 75%,rgba(233,236,240,0) 100%)}
.hero-title{left:132px;top:174px;color:var(--brand);font-size:21.5px;font-weight:600;line-height:24px}
.hero-title span{display:block;padding-left:67px}
.hero-rule{left:142px;top:232px;width:251px;height:1px;background:var(--brand-dark)}
.hero-text{left:136px;top:240px;width:320px;font-size:10.5px;line-height:16.7px;color:#555}
.btn{display:block;border:1px solid var(--brand);color:var(--brand);font-size:10.5px;text-align:center;background:var(--white);text-decoration:none}
.hero-btn{left:135px;top:292px;width:84px;height:25px;line-height:23px}
.services{left:0;top:420px;width:1055px;height:294px;background:var(--band)}
.service{width:184px}
.service-photo{width:184px;height:126px;border:1px solid #ddd}
.service h3{margin-top:16px;font-size:12.3px;font-weight:400;color:var(--brand)}
.service p{margin-top:10px;padding-left:2px;font-size:9.8px;line-height:18.4px;color:var(--muted)}
.read-more{margin-top:6px;padding-left:2px;display:flex;align-items:center;gap:8px;font-size:10px;color:var(--muted)}
.read-more.is-active{color:var(--brand)}
.welcome{left:0;top:714px;width:1055px;height:306px;background:var(--warm)}
.welcome-title{left:136px;top:748px;font-size:25px;font-weight:400;color:var(--brand-dark)}
.welcome-title .brand-name{color:var(--brand);font-weight:700}
.welcome-text{left:136px;top:797px;width:512px;font-size:10.5px;line-height:18.4px;color:#555}
.welcome-text p+p{margin-top:18.4px}
.welcome-btn{left:136px;top:960px;width:83px;height:25px;line-height:23px}
.news-title{left:668px;top:748px;font-size:20px;font-weight:400;color:var(--brand-dark)}
.news-item{left:670px;width:251px;display:flex;gap:14px;border-bottom:1px solid #cfcfcf}
.news-photo{width:67px;height:65px;flex:none}
.news-item h4{font-size:12px;font-weight:400;color:#1a1a1a;margin-top:-3px}
.news-item h4.is-active{color:var(--brand)}
.news-date{font-size:7.8px;color:#222;margin-top:4px}
.news-item p{font-size:9.8px;line-height:15px;color:var(--muted);margin-top:5px;padding-left:2px}
.footer{left:0;top:1020px;width:1055px;height:151px;background:var(--footer);color:var(--white)}
.footer-logo{left:134px;top:1045px;color:var(--white);font-size:27px}
.footer-rule{left:134px;top:1084px;width:92px;height:1px;background:#c8c8c8}
.footer-address{left:134px;top:1086px;font-size:9.8px;line-height:18px;color:var(--white)}
.footer-address .label{margin-bottom:7px}
.footer-col{top:1041px;font-size:10px}
.footer-col h5{font-size:12px;font-weight:600;margin-bottom:6px}
.footer-col li{list-style:none;line-height:15.2px;display:flex;align-items:center;gap:8px}
.bottom-bar{left:0;top:1171px;width:1055px;height:29px;background:var(--brand);color:var(--white);font-size:10px}
.copyright{left:134px;top:1179px;color:var(--white);font-size:10px}
.socialize{left:761px;top:1178px;display:flex;align-items:center;gap:5px;color:var(--white);font-size:10px}
.social-dot{width:16px;height:16px;border-radius:50%;background:var(--white)}
.socialize span{margin-right:3px}
</style>
</head>
<body>
<div class="page">
  <div class="abs top-rule"></div>
  <header class="abs header"></header>
  <div class="abs members-login">Members Login</div>
  <div class="abs logo site-logo">Vantor-o</div>
  <nav class="abs nav">
    <a class="active" href="#">Home</a>
    <a href="#">About Us</a>
    <a href="#">Services
      <svg width="8" height="6" viewBox="0 0 8 6"><path d="M1 1l3 3 3-3" fill="none" stroke="#555" stroke-width="1.3"/></svg></a>
    <a href="#">Our Clients</a>
    <a href="#">Blog</a>
    <a href="#">Contact Us</a>
  </nav>

  <section class="abs hero"></section>
  <div class="abs hero-photo" role="img" aria-label="Photo of a consulting team in business suits standing in a bright office"></div>
  <h1 class="abs hero-title">Vantor-o is a professional<span>Services organisation</span></h1>
  <div class="abs hero-rule"></div>
  <p class="abs hero-text">Many desktop publishing packages and web page editors now use Lorem Ipsum as their default model text,</p>
  <a class="abs btn hero-btn" href="#">Read more</a>

  <section class="abs services"></section>
  <article class="abs service" style="left:134px;top:446px">
    <div class="service-photo" role="img" aria-label="Photo of a consultant leading a workshop around a meeting table" style="background:linear-gradient(135deg,#f4f4f4,#d9d6d2 60%,#8a8378)"></div>
    <h3>Project Management</h3>
    <p>There are many variations of passages of Lorem Ipsum, but the majority have suffered alteration in some form.</p>
    <div class="read-more">Read more <svg width="16" height="6" viewBox="0 0 16 6"><path d="M0 3h13M10 0.5l4 2.5-4 2.5" fill="none" stroke="#8a8a8a" stroke-width="1.4"/></svg></div>
  </article>
  <article class="abs service" style="left:335px;top:446px">
    <div class="service-photo" role="img" aria-label="Photo of colleagues collaborating over a laptop and documents on a desk" style="background:linear-gradient(135deg,#3a2a2a,#6b3b3b 45%,#c9c3bd)"></div>
    <h3>Business Process Management</h3>
    <p>There are many variations of passages of Lorem Ipsum, but the majority have suffered alteration in some form.</p>
    <div class="read-more is-active">Read more <svg width="16" height="6" viewBox="0 0 16 6"><path d="M0 3h13M10 0.5l4 2.5-4 2.5" fill="none" stroke="#0d4f9c" stroke-width="1.6"/></svg></div>
  </article>
  <article class="abs service" style="left:536px;top:446px">
    <div class="service-photo" role="img" aria-label="Top-down photo of a team reviewing papers and a tablet on a white table" style="background:linear-gradient(135deg,#e9e9e9,#bdbdbd 50%,#6f6f6f)"></div>
    <h3>Change Management</h3>
    <p>There are many variations of passages of Lorem Ipsum, but the majority have suffered alteration in some form.</p>
    <div class="read-more">Read more <svg width="16" height="6" viewBox="0 0 16 6"><path d="M0 3h13M10 0.5l4 2.5-4 2.5" fill="none" stroke="#8a8a8a" stroke-width="1.4"/></svg></div>
  </article>
  <article class="abs service" style="left:737px;top:446px">
    <div class="service-photo" role="img" aria-label="Photo of a consultant presenting a chart on a flipboard to colleagues" style="background:linear-gradient(135deg,#f2f2f2,#cfd2d6 50%,#2f3540)"></div>
    <h3>Business Analytics</h3>
    <p>There are many variations of passages of Lorem Ipsum, but the majority have suffered alteration in some form.</p>
    <div class="read-more">Read more <svg width="16" height="6" viewBox="0 0 16 6"><path d="M0 3h13M10 0.5l4 2.5-4 2.5" fill="none" stroke="#8a8a8a" stroke-width="1.4"/></svg></div>
  </article>

  <section class="abs welcome"></section>
  <h2 class="abs welcome-title">Welcome to <span class="brand-name">Vantor-o</span></h2>
  <div class="abs welcome-text">
    <p>Contrary to popular belief, Lorem Ipsum is not simply random text. It has roots in a piece of classical Latin literature from 45 BC, making it over 2000 years old. Edwin Harlow, a Latin professor at Brookfield College in Vermont, looked up one of the more obscure Latin words, consectetur, from a Lorem Ipsum passage, and going through the cites of the word in classical literature, discovered the undoubtable source.</p>
    <p>Lorem Ipsum passage, and going through the cites of the word in classical literature, discovered the undoubtable source.</p>
  </div>
  <a class="abs btn welcome-btn" href="#">Read more</a>

  <h2 class="abs news-title">Latest News</h2>
  <article class="abs news-item" style="top:799px;height:80px">
    <div class="news-photo" role="img" aria-label="Photo of business people racing across a finish line" style="background:linear-gradient(135deg,#7a9a5a,#b04a3e 55%,#2c2c2c)"></div>
    <div>
      <h4>Lorem Ipsum Simply Dummy</h4>
      <div class="news-date">19 March 2014, 20:30</div>
      <p>Lorem Ipsum has been the industry's standard dummy text</p>
    </div>
  </article>
  <article class="abs news-item" style="top:903px;height:77px">
    <div class="news-photo" role="img" aria-label="Photo of a businesswoman seated at a desk" style="background:linear-gradient(135deg,#d9b48a,#6b4a32 50%,#f1ece6)"></div>
    <div>
      <h4 class="is-active">Lorem Ipsum Simply Dummy</h4>
      <div class="news-date">17 Feb 2014, 20:30</div>
      <p>Lorem Ipsum has been the industry's standard dummy text</p>
    </div>
  </article>

  <footer class="abs footer"></footer>
  <div class="abs logo footer-logo">Vantor-o</div>
  <div class="abs footer-rule"></div>
  <address class="abs footer-address" style="font-style:normal">
    <div class="label">Address:</div>
    214 Larkspur Row,<br>Hollin, HL 22 Qd 18.<br>Phone: + 61 400 000 182
  </address>
  <div class="abs footer-col" style="left:335px">
    <h5>Company</h5>
    <ul>
      <li><svg width="4" height="7" viewBox="0 0 4 7"><path d="M.5 .5l3 3-3 3" fill="none" stroke="#fff"/></svg>About Us</li>
      <li><svg width="4" height="7" viewBox="0 0 4 7"><path d="M.5 .5l3 3-3 3" fill="none" stroke="#fff"/></svg>Clients</li>
      <li><svg width="4" height="7" viewBox="0 0 4 7"><path d="M.5 .5l3 3-3 3" fill="none" stroke="#fff"/></svg>Presentation</li>
      <li><svg width="4" height="7" viewBox="0 0 4 7"><path d="M.5 .5l3 3-3 3" fill="none" stroke="#fff"/></svg>Support</li>
      <li><svg width="4" height="7" viewBox="0 0 4 7"><path d="M.5 .5l3 3-3 3" fill="none" stroke="#fff"/></svg>Schedule</li>
    </ul>
  </div>
  <div class="abs footer-col" style="left:469px">
    <h5>Overview</h5>
    <ul>
      <li><svg width="4" height="7" viewBox="0 0 4 7"><path d="M.5 .5l3 3-3 3" fill="none" stroke="#fff"/></svg>What we do</li>
      <li><svg width="4" height="7" viewBox="0 0 4 7"><path d="M.5 .5l3 3-3 3" fill="none" stroke="#fff"/></svg>News</li>
      <li><svg width="4" height="7" viewBox="0 0 4 7"><path d="M.5 .5l3 3-3 3" fill="none" stroke="#fff"/></svg>Presentation</li>
      <li><svg width="4" height="7" viewBox="0 0 4 7"><path d="M.5 .5l3 3-3 3" fill="none" stroke="#fff"/></svg>Solutions</li>
    </ul>
  </div>
  <div class="abs footer-col" style="left:603px">
    <h5>Navigations</h5>
    <ul>
      <li><svg width="4" height="7" viewBox="0 0 4 7"><path d="M.5 .5l3 3-3 3" fill="none" stroke="#fff"/></svg>About Us</li>
      <li><svg width="4" height="7" viewBox="0 0 4 7"><path d="M.5 .5l3 3-3 3" fill="none" stroke="#fff"/></svg>Clients</li>
      <li><svg width="4" height="7" viewBox="0 0 4 7"><path d="M.5 .5l3 3-3 3" fill="none" stroke="#fff"/></svg>Presentation</li>
      <li><svg width="4" height="7" viewBox="0 0 4 7"><path d="M.5 .5l3 3-3 3" fill="none" stroke="#fff"/></svg>Support</li>
      <li><svg width="4" height="7" viewBox="0 0 4 7"><path d="M.5 .5l3 3-3 3" fill="none" stroke="#fff"/></svg>Schedule</li>
    </ul>
  </div>
  <div class="abs footer-col" style="left:737px">
    <h5>For Clients</h5>
    <ul>
      <li><svg width="4" height="7" viewBox="0 0 4 7"><path d="M.5 .5l3 3-3 3" fill="none" stroke="#fff"/></svg>Home</li>
      <li><svg width="4" height="7" viewBox="0 0 4 7"><path d="M.5 .5l3 3-3 3" fill="none" stroke="#fff"/></svg>About Us</li>
      <li><svg width="4" height="7" viewBox="0 0 4 7"><path d="M.5 .5l3 3-3 3" fill="none" stroke="#fff"/></svg>Services</li>
      <li><svg width="4" height="7" viewBox="0 0 4 7"><path d="M.5 .5l3 3-3 3" fill="none" stroke="#fff"/></svg>Projects</li>
      <li><svg width="4" height="7" viewBox="0 0 4 7"><path d="M.5 .5l3 3-3 3" fill="none" stroke="#fff"/></svg>Blog</li>
      <li><svg width="4" height="7" viewBox="0 0 4 7"><path d="M.5 .5l3 3-3 3" fill="none" stroke="#fff"/></svg>Contacts</li>
    </ul>
  </div>

  <div class="abs bottom-bar"></div>
  <div class="abs copyright">Vantor - o © 2014 | PRIVACY POLICY</div>
  <div class="abs socialize">
    <span>Be Socialize with us:</span>
    <i class="social-dot" aria-label="friendwall"></i>
    <i class="social-dot" aria-label="chirpline"></i>
    <i class="social-dot" aria-label="workmesh"></i>
  </div>
</div>
</body>
</html>
```